Ramadan Kareem Graphic

Seeking a branded graphic to send to clients by email and social media wishing them a happy Ramadan. Having the text in English is acceptable but some Arabic would be preferred. Attaching the company logo which should be included in some form.

Target Market(s)

Government and commercial clients

Font styles to use
Serif
Sans Serif
Decorative
Script

Requirements
Must have
• My company logo, Halvern Guard Systems LLC
Nice to have
• Arabic text or calligraphy

```html
<!DOCTYPE html>
<html lang="en">
<head>
<meta charset="utf-8">
<title>Ramadan Kareem – Halvern Guard Systems LLC</title>
<link rel="stylesheet" href="https://fonts.googleapis.com/css2?family=Poiret+One&family=Tajawal:wght@400;500&family=Montserrat:wght@400;500&display=swap">
<style>
  :root {
    --bg: #113a3b;
    --bg-deep: #0c2f31;
    --gold: #c9a66b;
    --gold-light: #e2c48c;
    --gold-dark: #a9834c;
    --accent: #ee936b;
    --rule: #cfd4d5;
    --ink: #ffffff;
  }
  * { margin: 0; padding: 0; box-sizing: border-box; }
  html, body { width: 687px; height: 1200px; overflow: hidden; background: var(--bg); }
  .greeting-card {
    position: relative;
    width: 687px;
    height: 1200px;
    overflow: hidden;
    background: linear-gradient(180deg, var(--bg) 0%, #123d3e 50%, var(--bg-deep) 100%);
  }
  .brand {
    position: absolute;
    left: 28px;
    top: 30px;
    display: flex;
    align-items: center;
    gap: 12px;
  }
  .brand-name {
    font-family: "Montserrat", sans-serif;
    font-weight: 500;
    font-size: 19px;
    line-height: 1.25;
    color: var(--ink);
    width: 190px;
  }
  .brand-dot {
    flex: none;
    width: 14px;
    height: 14px;
    border-radius: 50%;
    background: var(--accent);
  }
  .arch-frame {
    position: absolute;
    left: 0;
    top: 0;
    width: 687px;
    height: 960px;
  }
  .ornaments {
    position: absolute;
    left: 55px;
    top: 0;
    width: 600px;
    height: 960px;
    background:
      radial-gradient(circle at 22% 20%, rgba(13,70,70,0.9) 0 70px, transparent 72px),
      radial-gradient(circle at 105px 420px, rgba(201,166,107,0.45) 0 60px, transparent 62px),
      radial-gradient(circle at 490px 250px, rgba(201,166,107,0.4) 0 55px, transparent 70px),
      radial-gradient(circle at 75px 730px, rgba(201,166,107,0.4) 0 55px, transparent 70px),
      radial-gradient(circle at 440px 810px, rgba(201,166,107,0.5) 0 85px, transparent 100px),
      radial-gradient(circle at 520px 680px, rgba(13,70,70,0.9) 0 75px, transparent 77px);
  }
  .calligraphy {
    position: absolute;
    left: 255px;
    top: 245px;
    width: 200px;
    height: 225px;
    border-radius: 50%;
    background: radial-gradient(ellipse at center, rgba(201,166,107,0.35) 0%, rgba(201,166,107,0.12) 55%, transparent 72%);
  }
  .headline {
    position: absolute;
    left: 203px;
    top: 505px;
    font-family: "Poiret One", sans-serif;
    font-weight: 400;
    color: var(--gold-light);
    line-height: 1;
  }
  .headline .line-1 { display: block; font-size: 66px; margin-left: 34px; }
  .headline .line-2 { display: block; font-size: 98px; margin-top: -6px; }
  .signature {
    position: absolute;
    left: 25px;
    top: 962px;
    font-family: "Tajawal", sans-serif;
    color: var(--ink);
    direction: rtl;
    text-align: left;
  }
  .signature .person { font-size: 31px; font-weight: 500; line-height: 1.2; }
  .signature .role { font-size: 21px; margin-top: 14px; line-height: 1.2; }
  .divider {
    position: absolute;
    left: 22px;
    top: 1051px;
    width: 661px;
    height: 5px;
    background: var(--rule);
  }
  .divider::before {
    content: "";
    position: absolute;
    left: 0; top: 0;
    width: 92px; height: 5px;
    background: var(--accent);
  }
  .contact {
    position: absolute;
    display: flex;
    align-items: center;
    gap: 9px;
    font-family: "Montserrat", sans-serif;
    font-size: 17px;
    color: var(--ink);
  }
  .contact .icon {
    flex: none;
    width: 36px;
    height: 36px;
    border-radius: 50%;
    background: var(--accent);
    display: flex;
    align-items: center;
    justify-content: center;
  }
  .contact .label { font-family: "Tajawal", sans-serif; font-size: 20px; }
  .contact-qatar { left: 65px; top: 1086px; }
  .contact-us { left: 383px; top: 1084px; }
  .contact-email { left: 227px; top: 1157px; }
</style>
</head>
<body>
<main class="greeting-card">
  <div class="brand">
    <span class="brand-name">Halvern Guard Systems LLC</span>
    <span class="brand-dot"></span>
  </div>

  <div class="ornaments" role="img" aria-label="Hanging gold lanterns, crescent moon, dotted teal spheres and gold geometric star flowers around the arch"></div>

  <svg class="arch-frame" viewBox="0 0 687 960" aria-hidden="true">
    <path d="M112 250 C160 240 200 225 228 185 C270 170 320 130 350 108 C380 130 430 160 470 182 C510 200 560 225 590 242 L590 760 C540 800 470 850 410 880 C390 910 370 930 350 940 C330 920 300 880 260 850 C230 820 180 812 112 800 Z"
          fill="none" stroke="var(--gold)" stroke-width="11" stroke-linejoin="round"/>
  </svg>

  <div class="calligraphy" role="img" aria-label="Gold Arabic calligraphy reading Ramadan Kareem"></div>

  <h1 class="headline">
    <span class="line-1">Ramadan</span>
    <span class="line-2">Kareem</span>
  </h1>

  <div class="signature">
    <p class="person">سامر خليل</p>
    <p class="role">المدير التنفيذي</p>
  </div>

  <div class="divider"></div>

  <div class="contact contact-qatar">
    <span class="icon"><svg width="18" height="18" viewBox="0 0 24 24"><path fill="#fff" d="M6.6 10.8a15.1 15.1 0 0 0 6.6 6.6l2.2-2.2a1 1 0 0 1 1-.25 11.4 11.4 0 0 0 3.6.57 1 1 0 0 1 1 1V20a1 1 0 0 1-1 1A17 17 0 0 1 3 4a1 1 0 0 1 1-1h3.5a1 1 0 0 1 1 1c0 1.25.2 2.450.57 3.57a1 1 0 0 1-.25 1z"/></svg></span>
    <span class="label">دولة قطر</span>
    <span class="number">+974.5550.0182</span>
  </div>

  <div class="contact contact-us">
    <span class="icon"><svg width="18" height="18" viewBox="0 0 24 24"><path fill="#fff" d="M6.6 10.8a15.1 15.1 0 0 0 6.6 6.6l2.2-2.2a1 1 0 0 1 1-.25 11.4 11.4 0 0 0 3.6.57 1 1 0 0 1 1 1V20a1 1 0 0 1-1 1A17 17 0 0 1 3 4a1 1 0 0 1 1-1h3.5a1 1 0 0 1 1 1c0 1.25.2 2.45.57 3.57a1 1 0 0 1-.25 1z"/></svg></span>
    <span class="label">نحن</span>
    <span class="number">+001 555.010.2200</span>
  </div>

  <div class="contact contact-email">
    <span class="icon"><svg width="18" height="14" viewBox="0 0 24 18"><path fill="#fff" d="M2 0h20a2 2 0 0 1 2 2v14a2 2 0 0 1-2 2H2a2 2 0 0 1-2-2V2a2 2 0 0 1 2-2zm0 3v.3l10 6.4 10-6.4V3L12 9.2z"/></svg></span>
    <span class="label">سامر@هالفرن.كوم</span>
  </div>
</main>
</body>
</html>
```